Buch-/E-Book-Cover für Sachbuch über Hunderasse
Zielgruppe
Ich benötige ein Buch-Cover im DIN A5 Format für ein anspruchsvolles Sachbuch, das die rassetypischen Krankheiten der Hunderasse Rhodesian Ridgeback thematisiert. Die Zielgruppe sind Züchter, Tierärzte und Liebhaber der Rasse.
Aufgabenstellung
Den größten Raum sollte ein Foto der Rasse einnehmen. Das Foto würde ich stellen, im Entwurf kann also ein Beispielfoto verwendet werden. Da das Buch der Auftakt zu einer Reihe ist, sollte das Design einen hohen Wiedererkennungswert haben und in erster Linie seriös wirken. Das Foto, der Rassename und die verwendeten Farben sollten leicht austauschbar sein. Sowohl der Titel als auch der Untertitel sind recht lang. Der Arbeitstitel lautet: Stille Pfade im Nebel der Ostseeküste, Untertitel: Geschichten von Fischern und Leuchttürmen.

```html
<!DOCTYPE html>
<html lang="de">
<head>
<meta charset="utf-8">
<title>Stille Pfade im Nebel der Ostseeküste – Buchcover</title>
<link rel="stylesheet" href="https://fonts.googleapis.com/css2?family=Istok+Web:wght@400;700&display=swap">
<style>
  :root {
    --stage: #d9d9d9;
    --teal: #3f8ea3;
    --teal-deep: #387f92;
    --lime: #a9c64c;
    --paper: #ffffff;
    --photo-light: #f4f4f4;
    --photo-tone: 207, 141, 78;
    --text-light: #f2f5f6;
  }
  * { box-sizing: border-box; margin: 0; padding: 0; }
  html, body {
    width: 1200px;
    height: 900px;
    overflow: hidden;
    background: var(--stage);
    font-family: "Istok Web", Verdana, sans-serif;
  }
  .cover {
    position: absolute;
    left: 327px;
    top: 40px;
    width: 546px;
    height: 820px;
    background: var(--teal);
    display: flex;
    flex-direction: column;
  }
  .author-band {
    height: 72px;
    display: flex;
    align-items: center;
    background: var(--teal);
  }
  .author-band .accent {
    width: 58px;
    height: 100%;
    background: var(--lime);
  }
  .author-name {
    margin-left: 26px;
    color: var(--text-light);
    font-size: 23px;
    font-weight: 700;
    letter-spacing: 0.2px;
  }
  .cover-photo {
    height: 408px;
    background:
      radial-gradient(ellipse 44% 34% at 56% 46%,
        rgba(var(--photo-tone), 0.95) 0%,
        rgba(var(--photo-tone), 0.8) 45%,
        rgba(var(--photo-tone), 0) 100%),
      linear-gradient(180deg, var(--paper), var(--photo-light));
  }
  .divider {
    height: 4px;
    background: var(--lime);
  }
  .title-block {
    flex: 1;
    background: linear-gradient(180deg, var(--teal), var(--teal-deep));
    padding: 76px 30px 0 54px;
  }
  .book-title {
    color: var(--lime);
    font-size: 35px;
    font-weight: 700;
    line-height: 40px;
    letter-spacing: 0.3px;
  }
  .book-subtitle {
    margin-top: 32px;
    color: var(--text-light);
    font-size: 22px;
    font-weight: 700;
    line-height: 29px;
    letter-spacing: 0.4px;
  }
</style>
</head>
<body>
  <article class="cover">
    <header class="author-band">
      <span class="accent"></span>
      <span class="author-name">Autoren Name</span>
    </header>
    <div class="cover-photo" role="img" aria-label="Foto: Hund in Seitenansicht, stehend vor weißem Hintergrund"></div>
    <div class="divider"></div>
    <section class="title-block">
      <h1 class="book-title">Stille Pfade im Nebel<br>der Ostseeküste</h1>
      <p class="book-subtitle">Geschichten von Fischern und<br>Leuchttürmen</p>
    </section>
  </article>
</body>
</html>
```